Lanternfold Cybersecurity Web Site Project

Lanternfold Cybersecurity is an MSP provider that is a full-service IT delivery organization focused on service deliver and information security.

We are looking for CREATIVE and UNIQUE website design that lays out the initial landing page and content page for us to continue developing for our organization. We have attached a .zip of our logo and images stock for you to incorporate into the site.

We are a Cybersecurity / MSP focused on providing a full-service outsourced IT Services to organizations that also have information cybersecurity compliance requirements such as HIPAA, PCI-DSS,
NYS DFS 23 NYCRR 500.

Systems / Applications Solutions:
On-Premises and Cloud Solutions
IT Services / Help Desk
User and System Issue Resolution
CloudDesk Administration
Nimbra / Cloud Virtualization
Paneos / Tuxora Server Administration

We are looking for two (2) .psd design files for the landing page and content page based on the logo stock art provided and all files / artwork created by the designer at project completion.

Please be creative and make this site stand out from all others. We are well aware of template sites like Pixel Orchard and others like it, so please we are not looking for a template we could download ourselves.

Target Market(s)

Demographic: Law Firms, Legal Services, Small - Medium Doctor offices, Medical services companies, Finance, Mortgage, Securities.

Businesses looking to outsource their IT departments.
Move to a full cloud business solution.
Require cybersecurity compliance such as HIPAA, PCI-DSS or DFS 23 NYCRR 500.

Industry/Entity Type

Information Technology

Number of Pages Required

2 page

Requirements
Must have
• We have included stock art for logo's, banners, headers, footers, please use that graphic stock for the site.

We operate in the Managed Service Provider (MSP) and Cybersecurity space
Should not have
• Themes we can get from any of the theme sites out there. We are looking for something completely new and unique.

```html
<!DOCTYPE html>
<html lang="en">
<head>
<meta charset="utf-8">
<title>Lanternfold Cybersecurity — Managed IT Services</title>
<link rel="stylesheet" href="https://fonts.googleapis.com/css2?family=Lato:wght@300;400;700;900&family=Saira+Condensed:wght@600;700&family=Orbitron:wght@800&family=Raleway:wght@300;400&display=swap">
<style>
:root{
  --red:#b81f25;
  --red-deep:#8e1518;
  --navy:#141a2e;
  --navy-2:#1b2238;
  --ink:#1d2233;
  --text:#555a66;
  --grey-band:#e4e5e7;
  --footer-bar:#3a3f4e;
  --white:#ffffff;
}
*{margin:0;padding:0;box-sizing:border-box}
html,body{width:1200px;height:3856px;overflow:hidden;background:var(--white)}
body{font-family:"Lato",sans-serif;color:var(--text);position:relative}
.abs{position:absolute}
.topline{top:0;left:0;width:1200px;height:5px;background:var(--red)}

/* header */
.brand{display:flex;align-items:center;gap:12px}
.brand-dot{width:44px;height:44px;border-radius:50%;background:var(--red)}
.brand-name{font-family:"Lato",sans-serif;font-weight:900;color:var(--navy);font-size:24px;line-height:1;letter-spacing:1px;text-transform:uppercase}
.brand-name small{display:block;font-size:12px;letter-spacing:3px;margin-top:3px}
.header-phone{top:44px;left:762px;font-size:16px;color:var(--ink);display:flex;align-items:center;gap:7px}
.social-top{top:45px;left:963px;display:flex;gap:3px}
.social-top span{width:19px;height:19px;background:var(--red)}
.nav{top:78px;left:686px;display:flex;gap:22px;align-items:center;font-size:13.5px;color:var(--ink)}
.nav .active{background:var(--red);color:#fff;border-radius:10px;padding:3px 10px;font-weight:700}

/* hero */
.hero-photo{top:118px;left:0;width:1200px;height:545px;background:linear-gradient(90deg,#eef0f1 0%,#e9eaec 38%,#cdbfb4 55%,#a88a78 72%,#d8d6d3 100%)}
.hero-copy{top:305px;left:85px;font-family:"Raleway",sans-serif;color:var(--ink);font-weight:300}
.hero-copy .lead{font-size:33px;line-height:40px}
.hero-copy .headline{font-family:"Orbitron",sans-serif;font-weight:800;color:var(--red);font-size:33px;line-height:44px;letter-spacing:.5px}
.hero-more{top:510px;left:82px;width:92px;height:27px;background:var(--navy);border-radius:4px;color:#fff;font-size:12px;display:flex;align-items:center;gap:10px;padding-left:6px}
.hero-more i{width:22px;height:18px;background:var(--red);border-radius:3px}

/* section titles */
.section-title{left:0;width:1200px;text-align:center;font-family:"Saira Condensed",sans-serif;font-weight:700;font-size:52px;color:var(--navy);display:flex;justify-content:center;align-items:center;gap:18px;line-height:1}
.section-title b{color:var(--red);font-weight:700}
.section-title .mark{width:44px;height:44px;border-radius:50%;background:var(--red)}
.title-rule{left:570px;width:62px;height:2px;background:var(--red)}

/* welcome */
.welcome-photo{top:908px;left:127px;width:332px;height:242px;background:linear-gradient(135deg,#3a4a72,#5e7bb0 50%,#2a3556)}
.welcome-text{top:903px;left:495px;width:565px;font-size:11.5px;line-height:16px;color:#555}
.welcome-text p{margin-bottom:14px}
.checks{top:1027px;left:497px;display:grid;grid-template-columns:210px 210px;row-gap:7px;font-size:11.5px;color:var(--red);text-transform:uppercase}
.checks li{list-style:none;display:flex;align-items:center;gap:8px}
.checks svg{flex:none}
.btn-read{display:flex;align-items:center;background:var(--red);color:#fff;font-size:10px;border-radius:4px;height:26px;overflow:hidden}
.btn-read span{padding:0 10px}
.btn-read i{background:var(--navy);width:22px;height:26px;display:flex;align-items:center;justify-content:center;font-style:normal;font-size:13px}

/* services */
.services-intro{top:1480px;left:105px;width:1000px;font-size:12px;line-height:16px;color:#555}
.hub{top:1652px;left:448px;width:302px;height:302px;border-radius:50%;background:var(--navy);border:8px solid #fff;box-shadow:0 0 0 3px var(--navy)}
.hub-name{top:1790px;left:448px;width:302px;text-align:center;color:#fff;font-weight:700;font-size:20px;letter-spacing:1px}
.svc{font-size:17px;line-height:18px;color:var(--ink);display:flex;align-items:center;gap:10px}
.svc.right-al{text-align:right}
.icon-sq{width:30px;height:30px;background:var(--red);border-radius:3px}
.spoke{width:2px;height:22px;background:var(--ink)}

/* testimonials */
.quote{top:2350px;left:300px;width:600px;text-align:center;font-size:12.5px;line-height:20px;color:#555}
.quote q{quotes:none}
.qmark{font-family:Georgia,serif;color:var(--red);font-size:38px;font-weight:900;line-height:1}
.person{top:2432px;left:0;width:1200px;text-align:center}
.person strong{display:block;color:var(--red);font-weight:400;font-size:15px}
.person span{font-size:11px;color:#333}

/* cta */
.cta-copy{top:2840px;left:0;width:1200px;text-align:center;color:#fff}
.cta-copy .kicker{font-family:"Saira Condensed",sans-serif;font-weight:600;font-size:33px;letter-spacing:.3px}
.cta-copy .big{font-family:"Lato",sans-serif;font-weight:700;font-size:48px;line-height:56px}

/* partners */
.partners{top:3255px;left:255px;display:flex;gap:70px;align-items:center}
.partners span{background:#c5c7cc;border-radius:4px}

/* footer */
.footer{top:3400px;left:0;width:1200px;height:390px;background:var(--navy)}
.foot-col{color:#fff}
.foot-head{color:var(--red);font-size:17px;font-weight:700;padding-bottom:10px;border-bottom:1px dotted #777;width:140px}
.foot-links{list-style:none;margin-top:18px;font-size:15px;line-height:26.5px}
.foot-links li::before{content:"‹";color:var(--red);margin-right:9px}
.foot-contact{margin-top:18px;font-size:11.5px;line-height:19px}
.divider{width:1px;height:200px;background:#4a5068}
.copyright{top:3790px;left:0;width:1200px;height:66px;background:var(--footer-bar);color:#dfe0e4;font-size:14px;display:flex;align-items:center;justify-content:center}
</style>
</head>
<body>

<div class="abs topline"></div>

<!-- header -->
<header>
  <div class="abs brand" style="top:36px;left:80px">
    <span class="brand-dot"></span>
    <span class="brand-name">Lanternfold<small>Cybersecurity</small></span>
  </div>
  <div class="abs header-phone">
    <svg width="13" height="13" viewBox="0 0 24 24"><path fill="#b81f25" d="M6.6 10.8a15 15 0 006.6 6.6l2.2-2.2c.3-.3.7-.4 1-.2 1.1.4 2.3.6 3.6.6.6 0 1 .4 1 1V20c0 .6-.4 1-1 1A17 17 0 013 4c0-.6.4-1 1-1h3.5c.6 0 1 .4 1 1 0 1.3.2 2.5.6 3.6.1.3 0 .7-.2 1z"/></svg>
    (555) 214 7730
  </div>
  <div class="abs social-top"><span></span><span></span><span></span><span></span></div>
  <nav class="abs nav">
    <span class="active">Home</span><span>about</span><span>services</span><span>contact</span><span>customer support</span><span>login</span>
  </nav>
</header>

<!-- hero -->
<section>
  <div class="abs hero-photo" role="img" aria-label="Photo of a smiling support agent wearing a headset"></div>
  <svg class="abs" style="top:560px;left:0" width="1200" height="110" viewBox="0 0 1200 110">
    <path d="M0 20 Q600 170 1200 20 L1200 110 L0 110Z" fill="#fff"/>
    <path d="M0 20 Q600 150 1200 22 L1200 35 Q600 175 0 30Z" fill="#b81f25"/>
  </svg>
  <div class="abs hero-copy">
    <div class="lead">Complete</div>
    <div class="headline">MANAGED IT SERVICES</div>
    <div class="lead">Solutions to grow your Business &amp;<br>Protect your valuable data</div>
  </div>
  <div class="abs hero-more"><i></i>MORE</div>
</section>

<!-- welcome -->
<section>
  <h2 class="abs section-title" style="top:776px"><span class="mark"></span><span>WELCOME TO <b>LANTERNFOLD</b></span></h2>
  <div class="abs title-rule" style="top:849px"></div>
  <div class="abs welcome-photo" role="img" aria-label="Photo of two engineers working in a server room"></div>
  <div class="abs welcome-text">
    <p>Lorem ipsum dolor sit amet, consectetur adipiscing elit, sed do eiusmod tempor incididunt ut labore et dolore magna aliqua. Ut enim ad minim veniam, quis nostrud exercitation ullamco laboris nisi</p>
    <p>ut aliquip ex ea commodo consequat. Duis aute irure dolor in reprehenderit in voluptate velit esse cillum dolore eu fugiat nulla pariatur. Ut enim ad minim veniam, quis nostrud exercitation ullamco laboris nisi</p>
  </div>
  <ul class="abs checks">
    <li><svg width="15" height="15" viewBox="0 0 16 16"><circle cx="8" cy="8" r="7" fill="none" stroke="#b81f25" stroke-width="1.3"/><path d="M4.8 8.2l2.2 2.2 4.2-4.4" fill="none" stroke="#b81f25" stroke-width="1.4"/></svg>Digital Transformation</li>
    <li><svg width="15" height="15" viewBox="0 0 16 16"><circle cx="8" cy="8" r="7" fill="none" stroke="#b81f25" stroke-width="1.3"/><path d="M4.8 8.2l2.2 2.2 4.2-4.4" fill="none" stroke="#b81f25" stroke-width="1.4"/></svg>Storage Solutions</li>
    <li><svg width="15" height="15" viewBox="0 0 16 16"><circle cx="8" cy="8" r="7" fill="none" stroke="#b81f25" stroke-width="1.3"/><path d="M4.8 8.2l2.2 2.2 4.2-4.4" fill="none" stroke="#b81f25" stroke-width="1.4"/></svg>Managed IT</li>
    <li><svg width="15" height="15" viewBox="0 0 16 16"><circle cx="8" cy="8" r="7" fill="none" stroke="#b81f25" stroke-width="1.3"/><path d="M4.8 8.2l2.2 2.2 4.2-4.4" fill="none" stroke="#b81f25" stroke-width="1.4"/></svg>Protect Data</li>
    <li><svg width="15" height="15" viewBox="0 0 16 16"><circle cx="8" cy="8" r="7" fill="none" stroke="#b81f25" stroke-width="1.3"/><path d="M4.8 8.2l2.2 2.2 4.2-4.4" fill="none" stroke="#b81f25" stroke-width="1.4"/></svg>Help Desk</li>
    <li><svg width="15" height="15" viewBox="0 0 16 16"><circle cx="8" cy="8" r="7" fill="none" stroke="#b81f25" stroke-width="1.3"/><path d="M4.8 8.2l2.2 2.2 4.2-4.4" fill="none" stroke="#b81f25" stroke-width="1.4"/></svg>Enable Compliance</li>
  </ul>
  <div class="abs btn-read" style="top:1121px;left:495px"><span>READ MORE</span><i>›</i></div>
</section>

<!-- services -->
<section>
  <svg class="abs" style="top:1225px;left:0" width="1200" height="870" viewBox="0 0 1200 870">
    <path d="M0 5 Q600 60 1200 5 L1200 870 L0 870Z" fill="#e4e5e7"/>
  </svg>
  <h2 class="abs section-title" style="top:1366px"><span class="mark"></span><span>OUR <b>SERVICES</b></span></h2>
  <div class="abs title-rule" style="top:1438px"></div>
  <p class="abs services-intro">Lorem ipsum dolor sit amet, consectetur adipiscing elit, sed do eiusmod tempor incididunt ut labore et dolore magna aliqua. Ut enim ad minim veniam, quis nostrud exercitation ullamco laboris nisi ut aliquip ex ea commodo consequat. Duis aute irure dolor in reprehenderit in voluptate velit esse cillum dolore eu fugiat nulla pariatur. Excepteur sint occaecat cupidatat non proident, sunt in culpa qui officia deserunt mollit anim id est laborum</p>

  <div class="abs hub"></div>
  <div class="abs hub-name">LANTERNFOLD</div>

  <!-- spokes -->
  <svg class="abs" style="top:1600px;left:400px" width="400" height="410" viewBox="0 0 400 410">
    <g stroke="#1d2233" stroke-width="2">
      <line x1="192" y1="22" x2="192" y2="42"/>
      <line x1="48" y1="112" x2="32" y2="100"/>
      <line x1="340" y1="112" x2="358" y2="100"/>
      <line x1="40" y1="262" x2="24" y2="274"/>
      <line x1="350" y1="262" x2="368" y2="274"/>
      <line x1="120" y1="355" x2="110" y2="370"/>
      <line x1="270" y1="355" x2="280" y2="370"/>
    </g>
  </svg>

  <div class="abs svc" style="top:1578px;left:502px">
    <svg width="44" height="40" viewBox="0 0 44 40"><path d="M10 28a8 8 0 010-16 11 11 0 0121-3 8 8 0 016 15" fill="none" stroke="#b81f25" stroke-width="2"/><g stroke="#1d2233" stroke-width="1.5"><line x1="16" y1="22" x2="16" y2="34"/><line x1="22" y1="22" x2="22" y2="36"/><line x1="28" y1="22" x2="28" y2="34"/></g></svg>
    <span>On-Premises &amp;<br>Cloud Solutions</span>
  </div>
  <div class="abs svc" style="top:1684px;left:190px">
    <span style="text-align:right">Systems<br>Applications Solutions</span>
    <svg width="46" height="40" viewBox="0 0 46 40"><rect x="3" y="6" width="34" height="24" fill="none" stroke="#1d2233" stroke-width="2"/><line x1="0" y1="34" x2="42" y2="34" stroke="#1d2233" stroke-width="2"/><circle cx="26" cy="12" r="6" fill="none" stroke="#b81f25" stroke-width="2"/></svg>
  </div>
  <div class="abs svc" style="top:1682px;left:780px">
    <svg width="36" height="40" viewBox="0 0 36 40"><path d="M6 22a12 12 0 0124 0" fill="none" stroke="#b81f25" stroke-width="3"/><rect x="3" y="20" width="7" height="11" rx="2" fill="#b81f25"/><rect x="26" y="20" width="7" height="11" rx="2" fill="#b81f25"/><path d="M8 36h20" stroke="#1d2233" stroke-width="2"/></svg>
    <span>IT Services<br>Help Desk</span>
  </div>
  <div class="abs svc" style="top:1863px;left:190px">
    <span style="text-align:right">Paneos / Tuxora<br>Server Administration</span>
    <svg width="36" height="36" viewBox="0 0 36 36"><g fill="#b81f25"><rect x="0" y="2" width="36" height="9" rx="1"/><rect x="0" y="14" width="36" height="9" rx="1"/><rect x="0" y="26" width="36" height="9" rx="1"/></g></svg>
  </div>
  <div class="abs svc" style="top:1862px;left:782px">
    <svg width="42" height="38" viewBox="0 0 42 38"><rect x="2" y="4" width="38" height="26" fill="none" stroke="#1d2233" stroke-width="2"/><line x1="12" y1="35" x2="30" y2="35" stroke="#1d2233" stroke-width="2"/><circle cx="21" cy="17" r="7" fill="none" stroke="#b81f25" stroke-width="2.2"/></svg>
    <span>User &amp; System<br>Issue Resolution</span>
  </div>
  <div class="abs svc" style="top:1964px;left:334px">
    <span style="text-align:right">Nimbra / Cloud<br>Virtualization</span>
    <span class="icon-sq" style="width:40px;height:36px"></span>
  </div>
  <div class="abs svc" style="top:1964px;left:688px">
    <span class="icon-sq" style="width:28px;height:34px"></span>
    <span>CloudDesk<br>Administration</span>
  </div>
</section>

<!-- testimonials -->
<section>
  <h2 class="abs section-title" style="top:2254px"><span class="mark"></span><span>CLIENT <b>TESTIMONIALS</b></span></h2>
  <div class="abs title-rule" style="top:2324px"></div>
  <svg class="abs" style="top:2345px;left:76px" width="32" height="52" viewBox="0 0 32 52"><path d="M26 2L4 26l22 24" fill="none" stroke="#a9abb1" stroke-width="4"/></svg>
  <svg class="abs" style="top:2345px;left:1076px" width="32" height="52" viewBox="0 0 32 52"><path d="M6 2l22 24L6 50" fill="none" stroke="#a9abb1" stroke-width="4"/></svg>
  <div class="abs qmark" style="top:2346px;left:290px">“</div>
  <p class="abs quote"><q>Lorem ipsum dolor sit amet, consectetur adipiscing elit. Quid autem habent admirationis, cum prope accesseris?An hoc usque quaque, aliter in vita? Non igitur de improbo, sed de callidoim­probo quaerimus, qualis Q. Nam quibus rebus efficiuntur voluptates.</q></p>
  <div class="abs qmark" style="top:2390px;left:790px">”</div>
  <div class="abs person"><strong>MARCUS DELAVANE</strong><span>Regional Administration Director</span></div>
</section>

<!-- call to action -->
<section>
  <svg class="abs" style="top:2525px;left:0" width="1200" height="540" viewBox="0 0 1200 540" role="img" aria-label="Photo of business people shaking hands in an office, tinted red">
    <defs>
      <linearGradient id="ctaTone" x1="0" x2="1" y1="0" y2="1">
        <stop offset="0" stop-color="#b8625c"/>
        <stop offset=".5" stop-color="#a3403d"/>
        <stop offset="1" stop-color="#b45a55"/>
      </linearGradient>
    </defs>
    <path d="M0 12 Q600 70 1200 0 L1200 525 Q600 470 0 530Z" fill="url(#ctaTone)"/>
  </svg>
  <div class="abs cta-copy">
    <div class="kicker">ENSURE YOUR BUSINESS MEETS REGULATORY REQUIREMENT</div>
    <div class="big">Download free White Paper</div>
  </div>
  <svg class="abs" style="top:2944px;left:577px" width="44" height="52" viewBox="0 0 44 52">
    <path d="M4 2h26l10 10v36H4z" fill="none" stroke="#fff" stroke-width="2.5"/>
    <text x="22" y="24" fill="#fff" font-family="Lato,sans-serif" font-size="12" font-weight="700" text-anchor="middle">PDF</text>
    <path d="M22 30v14M15 38l7 7 7-7" fill="none" stroke="#fff" stroke-width="2.5"/>
  </svg>
</section>

<!-- partners -->
<section>
  <h2 class="abs section-title" style="top:3136px"><span class="mark"></span><span>OUR <b>PARTNERS</b></span></h2>
  <div class="abs title-rule" style="top:3206px"></div>
  <div class="abs partners">
    <span style="width:50px;height:56px"></span>
    <span style="width:120px;height:36px"></span>
    <span style="width:80px;height:40px"></span>
    <span style="width:120px;height:18px"></span>
    <span style="width:140px;height:40px"></span>
  </div>
</section>

<!-- footer -->
<footer>
  <svg class="abs" style="top:3370px;left:0" width="1200" height="80" viewBox="0 0 1200 80">
    <path d="M0 10 Q600 70 1200 10 L1200 80 L0 80Z" fill="#141a2e"/>
    <path d="M0 10 Q600 70 1200 10 L1200 30 Q600 90 0 30Z" fill="#b81f25"/>
  </svg>
  <div class="abs footer"></div>

  <div class="abs brand" style="top:3485px;left:90px">
    <span class="brand-dot"></span>
    <span class="brand-name" style="color:#fff">Lanternfold<small>Cybersecurity</small></span>
  </div>
  <p class="abs foot-col" style="top:3560px;left:90px;width:244px;font-size:11px;line-height:14px;text-align:justify">Lorem ipsum dolor sit amet, consectetur adipi­scing elit. Quid autem habent admirationis, cum prope accesseris? An hoc usque quaque, aliter in vita? Non igitur de improbo, sed de callido improbo quaerimus,</p>
  <div class="abs btn-read" style="top:3660px;left:90px;height:24px"><span>READ MORE</span><i style="background:var(--red);height:24px">›</i></div>

  <div class="abs divider" style="top:3478px;left:378px"></div>
  <div class="abs divider" style="top:3478px;left:625px"></div>
  <div class="abs divider" style="top:3478px;left:892px"></div>

  <div class="abs foot-col" style="top:3505px;left:433px">
    <div class="foot-head">QUICK LINKS</div>
    <ul class="foot-links"><li>Home</li><li>About us</li><li>Services</li><li>Customer Support</li><li>Contact us</li></ul>
  </div>

  <div class="abs foot-col" style="top:3505px;left:683px">
    <div class="foot-head" style="width:165px">CONTACT</div>
    <div class="foot-contact">42 Harbor Row<br>Millbrook, IL 60999</div>
    <div class="foot-contact" style="margin-top:10px;padding-left:19px;position:relative">
      <span style="position:absolute;left:0;color:var(--red)">●</span>555-214-7730<br>
      <span style="position:absolute;left:0;top:19px;color:var(--red)">▮</span>555-214-7731<br>
      <span style="position:absolute;left:0;top:38px;color:var(--red)">✉</span>hello@lanternfold.example<br>
      <span style="position:absolute;left:0;top:57px;color:var(--red)">●</span>www.lanternfold.example
    </div>
  </div>

  <div class="abs foot-col" style="top:3505px;left:945px">
    <div class="foot-head" style="width:165px">FOLLOW US ON</div>
    <div style="display:flex;gap:22px;margin-top:18px"><span style="width:10px;height:10px;background:var(--red)"></span><span style="width:10px;height:10px;background:var(--red)"></span><span style="width:10px;height:10px;background:var(--red)"></span><span style="width:10px;height:10px;background:var(--red)"></span></div>
    <div style="width:18px;height:1px;background:#aaa;margin-top:26px"></div>
    <div style="color:var(--red);font-weight:700;font-size:17px;margin-top:38px">CALL US ON</div>
    <div style="color:#fff;font-weight:900;font-size:21px;letter-spacing:.5px">555-214-7730</div>
  </div>

  <div class="abs copyright">© 2020 Lanternfold Cybersecurity &nbsp;|&nbsp; Privacy Policy &nbsp;|&nbsp; User Agreement</div>
</footer>

</body>
</html>
```